HPS business cards

(Generators . Lighting Towers . De-watering Pumps . Compressors) put under the logo please. my details are Owen Pritchard (Director) 0461527390 harbourpinesupply@postvale.net

```html
<!DOCTYPE html>
<html lang="en">
<head>
<meta charset="utf-8">
<title>HPS Business Cards</title>
<link href="https://fonts.googleapis.com/css2?family=Michroma&family=Lato:wght@400;700&display=swap" rel="stylesheet">
<style>
  :root {
    --page-bg: #2a2a2c;
    --card-bg: #1b1b1d;
    --gold: #f0a92a;
    --gold-light: #f7c744;
    --silver: #d9d9dc;
    --text-light: #e6e6e6;
    --text-muted: #b8b8bc;
    --rule: #c98a1c;
    --rule-dark: #555558;
  }
  * { box-sizing: border-box; margin: 0; padding: 0; }
  html, body {
    width: 1200px; height: 800px; overflow: hidden;
    background: var(--page-bg);
  }
  .canvas {
    position: relative; width: 1200px; height: 800px;
    display: flex; flex-direction: column; align-items: center; justify-content: center;
    gap: 40px;
  }
  .card {
    position: relative; width: 560px; height: 320px;
    background: var(--card-bg); border-radius: 22px; overflow: hidden;
    box-shadow: 0 10px 30px rgba(0,0,0,.45);
  }

  /* front */
  .card-front .edge-band {
    position: absolute; top: 0; right: 0; width: 14px; height: 100%;
    display: flex; flex-direction: column;
  }
  .edge-band .band-silver { flex: 0 0 62%; background: var(--silver); }
  .edge-band .band-ticks {
    flex: 0 0 5%;
    background: repeating-linear-gradient(to bottom, var(--silver) 0 2px, var(--card-bg) 2px 4px);
  }
  .edge-band .band-gold { flex: 1; background: var(--gold-light); }

  .brand {
    position: absolute; top: 30px; left: 0; right: 14px;
    display: flex; flex-direction: column; align-items: center; gap: 10px;
  }
  .brand-row { display: flex; align-items: center; gap: 12px; }
  .brand-mark { width: 24px; height: 24px; background: var(--gold); }
  .brand-name {
    font-family: "Michroma", sans-serif; font-size: 17px; letter-spacing: 1px;
    color: var(--gold); white-space: nowrap;
  }
  .brand-tagline {
    font-family: "Lato", sans-serif; font-size: 10px; letter-spacing: .6px;
    color: var(--text-muted); white-space: nowrap;
  }
  .brand-rule {
    position: absolute; top: 104px; left: 40px; right: 54px;
    height: 1px; background: var(--rule);
  }
  .person { position: absolute; left: 40px; top: 128px; right: 54px; }
  .person-name {
    font-family: "Michroma", sans-serif; font-size: 24px; font-weight: 400;
    color: var(--gold); letter-spacing: .5px; line-height: 1.3; white-space: nowrap;
  }
  .person-title {
    font-family: "Lato", sans-serif; font-size: 14px; color: var(--text-light);
    margin-top: 4px;
  }
  .person-rule { height: 1px; background: var(--rule); margin-top: 12px; }
  .contacts {
    list-style: none; margin-top: 14px;
    font-family: "Lato", sans-serif; font-size: 14px; color: var(--text-light);
  }
  .contacts li { display: flex; align-items: center; gap: 10px; margin-bottom: 8px; }
  .contacts svg { width: 14px; height: 14px; flex: none; }
  .icon-phone { fill: var(--gold); }
  .icon-mail { fill: none; stroke: var(--gold); stroke-width: 2; }

  /* back */
  .card-back { display: flex; align-items: center; justify-content: center; }
  .back-brand { display: flex; flex-direction: column; align-items: center; gap: 12px; }
  .back-brand-name {
    font-family: "Michroma", sans-serif; font-size: 26px; color: var(--silver);
    letter-spacing: 1.5px; white-space: nowrap;
  }
  .back-brand-tagline {
    font-family: "Lato", sans-serif; font-size: 11px; letter-spacing: .6px;
    color: var(--text-muted); white-space: nowrap;
  }
  .back-brand-rule { width: 380px; height: 1px; background: var(--rule-dark); }
</style>
</head>
<body>
<main class="canvas">
  <section class="card card-front" aria-label="Business card front">
    <div class="brand">
      <div class="brand-row">
        <span class="brand-mark"></span>
        <span class="brand-name">HARBOUR PINE SUPPLY</span>
      </div>
      <p class="brand-tagline">Generators . Lighting Towers . De-watering Pumps . Compressors</p>
    </div>
    <div class="brand-rule"></div>
    <div class="person">
      <h1 class="person-name">OWEN PRITCHARD</h1>
      <p class="person-title">Director</p>
      <div class="person-rule"></div>
      <ul class="contacts">
        <li>
          <svg class="icon-phone" viewBox="0 0 24 24" aria-hidden="true"><path d="M6.6 10.8a15.1 15.1 0 0 0 6.6 6.6l2.2-2.2a1 1 0 0 1 1-.25 11.4 11.4 0 0 0 3.6.57 1 1 0 0 1 1 1V20a1 1 0 0 1-1 1A17 17 0 0 1 3 4a1 1 0 0 1 1-1h3.5a1 1 0 0 1 1 1c0 1.25.2 2.45.57 3.57a1 1 0 0 1-.25 1z"/></svg>
          0461527390
        </li>
        <li>
          <svg class="icon-mail" viewBox="0 0 24 24" aria-hidden="true"><rect x="3" y="5" width="18" height="14"/><path d="M3 6l9 7 9-7"/></svg>
          harbourpinesupply@postvale.net
        </li>
      </ul>
    </div>
    <div class="edge-band">
      <span class="band-silver"></span>
      <span class="band-ticks"></span>
      <span class="band-gold"></span>
    </div>
  </section>

  <section class="card card-back" aria-label="Business card back">
    <div class="back-brand">
      <span class="back-brand-name">HARBOUR PINE SUPPLY</span>
      <p class="back-brand-tagline">Generators . Lighting Towers . De-watering Pumps . Compressors</p>
      <span class="back-brand-rule"></span>
    </div>
  </section>
</main>
</body>
</html>
```